The Grand Journeys of Tilda Barkaroo and Mabel Moo!

Have you ever wondered how a rescue puppy feels before and after being adopted?
Coming November 2015

The Grand Journeys of Tilda Barkaroo and Mabel Moo, Tilda gets her family

www.tildabarkaroo-example.com sign up to receive updates, special offers and enter contests!

Target Market(s)

children age 4-8, parents of children this age group 30-65

Industry/Entity Type

Publishing Company

Colors
33a6d7
6c459b
a64599

Requirements
Must have
• room for postage, a whimsical feel

```html
<!DOCTYPE html>
<html lang="en">
<head>
<meta charset="utf-8">
<title>The Grand Journeys of Tilda Barkaroo and Mabel Moo – Postcard</title>
<link rel="stylesheet" href="https://fonts.googleapis.com/css2?family=Didact+Gothic&family=Open+Sans:wght@400&display=swap">
<style>
  :root {
    --sky: #33a6d7;
    --violet: #6c459b;
    --orchid: #a64599;
    --ink: #3a3a3f;
    --navy: #1f2a4a;
    --paper: #ffffff;
    --stage: #e9e7ec;
    --rule: #c9c6cf;
  }
  * { margin: 0; padding: 0; box-sizing: border-box; }
  html, body { width: 900px; height: 1200px; overflow: hidden; }
  body {
    background: var(--stage);
    font-family: "Didact Gothic", sans-serif;
    color: var(--ink);
    position: relative;
  }
  .postcard {
    position: absolute;
    left: 30px;
    width: 840px;
    height: 525px;
    background: var(--paper);
    overflow: hidden;
    box-shadow: 0 2px 10px rgba(0,0,0,0.12);
  }
  .postcard--front { top: 45px; }
  .postcard--back { top: 630px; }

  .wash {
    position: absolute;
    left: 0; right: 0;
    pointer-events: none;
  }
  .wash--top {
    top: 0; height: 34px;
    background: linear-gradient(to bottom, rgba(108,69,155,0.55), rgba(166,69,153,0.15) 60%, rgba(255,255,255,0));
  }
  .wash--bottom {
    bottom: 0; height: 60px;
    background: linear-gradient(to top, rgba(108,69,155,0.85), rgba(166,69,153,0.45) 45%, rgba(255,255,255,0));
  }

  /* Front */
  .teaser {
    position: absolute;
    left: 86px; top: 62px;
    width: 520px;
    font-size: 31px;
    line-height: 1.22;
  }
  .teaser .hl-puppy { color: var(--orchid); }
  .teaser .hl-when { color: var(--violet); }
  .release {
    position: absolute;
    left: 86px; top: 228px;
    color: var(--sky);
    line-height: 1.1;
  }
  .release .label { display: block; font-size: 34px; }
  .release .date { display: block; font-size: 46px; }
  .book-title {
    position: absolute;
    left: 86px; top: 352px;
    font-size: 24px;
    line-height: 1.3;
  }
  .book-title .series { display: block; color: var(--violet); }
  .book-title .heroes { display: block; color: var(--orchid); }
  .book-title .episode { display: block; color: var(--sky); }
  .art-girl-puppy {
    position: absolute;
    left: 470px; top: 18px;
    width: 340px; height: 440px;
    border-radius: 40% 40% 30% 30%;
    background: radial-gradient(ellipse at 55% 40%, #b48fd0 0%, #d8c4e6 45%, rgba(255,255,255,0) 75%);
  }

  /* Back */
  .blurb {
    position: absolute;
    left: 34px; top: 46px;
    width: 420px;
    font-family: "Open Sans", sans-serif;
    font-size: 11.5px;
    line-height: 1.45;
    color: #4a4a50;
  }
  .blurb p + p { margin-top: 9px; }
  .art-butterfly {
    position: absolute;
    left: 20px; top: 200px;
    width: 330px; height: 200px;
    background: radial-gradient(ellipse at 45% 50%, rgba(214,170,120,0.55), rgba(180,150,200,0.25) 55%, rgba(255,255,255,0) 75%);
    border-radius: 50%;
  }
  .divider {
    position: absolute;
    left: 520px; top: 60px;
    width: 1px; height: 330px;
    background: var(--rule);
  }
  .stamp-box {
    position: absolute;
    right: 30px; top: 40px;
    width: 110px; height: 120px;
    border: 1.5px solid var(--rule);
  }
  .address-lines {
    position: absolute;
    left: 560px; top: 250px;
    width: 250px;
    list-style: none;
  }
  .address-lines li {
    height: 44px;
    border-bottom: 1.5px solid var(--rule);
  }
  .site-band {
    position: absolute;
    left: 30px; top: 398px;
    width: 470px; height: 40px;
    background: var(--navy);
    color: #fff;
    font-size: 24px;
    line-height: 40px;
    padding-left: 14px;
  }
  .signup {
    position: absolute;
    left: 30px; top: 442px;
    font-size: 24px;
    line-height: 1.15;
  }
  .signup .line-one { display: block; color: var(--sky); }
  .signup .line-two { display: block; color: var(--orchid); }
</style>
</head>
<body>

<section class="postcard postcard--front" aria-label="Postcard front">
  <div class="wash wash--top"></div>
  <div class="art-girl-puppy" role="img" aria-label="Illustration of a girl in a purple dress dancing with a black and white rescue puppy"></div>

  <h2 class="teaser">Have you ever wondered how a <span class="hl-puppy">rescue puppy</span> feels <span class="hl-when">before</span> and <span class="hl-when">after</span> being adopted?</h2>

  <p class="release">
    <span class="label">Coming</span>
    <span class="date">November 2015</span>
  </p>

  <h1 class="book-title">
    <span class="series">The Grand Journeys of</span>
    <span class="heroes">Tilda Barkaroo and Mabel Moo</span>
    <span class="episode">Tilda gets her family</span>
  </h1>

  <div class="wash wash--bottom"></div>
</section>

<section class="postcard postcard--back" aria-label="Postcard back">
  <div class="wash wash--top"></div>
  <div class="art-butterfly" role="img" aria-label="Faint watercolour illustration of a butterfly"></div>

  <div class="blurb">
    <p>This postcard shares news about our first picture book for young readers. Tilda is a small rescue puppy who learns that a loving home can change everything.</p>
    <p>Follow her story from the shelter to a cozy bed and a brand new best friend.</p>
    <p>Each page is filled with bright colors, gentle lessons and plenty of giggles for the whole family to enjoy together at bedtime.</p>
  </div>

  <div class="divider"></div>
  <div class="stamp-box" aria-label="Place stamp here"></div>
  <ul class="address-lines" aria-label="Address">
    <li></li><li></li><li></li>
  </ul>

  <p class="site-band">www.tildabarkaroo-example.com</p>
  <p class="signup">
    <span class="line-one">sign up to receive updates,</span>
    <span class="line-two">special offers and enter contests!</span>
  </p>

  <div class="wash wash--bottom"></div>
</section>

</body>
</html>
```